Web Design Project - Shipping Industry

Goals and Objectives
The objective of the new website is to create a more modern look and feel. The site will also allow for a more effective means of communicating with members while providing the public with information and developments in the local, regional and international shipping industry.
Scope
The website will highlight the history of the organisation inclusive of text and photographs. It will take visitors through the years from beginning to present. Information on the history of the shipping industry will also be included.
It will feature current articles on the organisation, its members and stakeholders in the shipping industry. Member information as well as pertinent details regarding the organisation’s subsidiaries will be documented for the website.
Information as it relates to shipping statistics, case studies, laws and regulations, international treaties and trade documents, shipping terms, careers in shipping, job opportunities, training opportunities, information for shippers including port listing and trade lanes will be main features of the content for the website.
The Association’s community involvement, industry calendar events and related links relevant industry members will also be featured.
Target Market
• The General Public;
• Members of the organization;
• Shipping Industry Stakeholders (local, regional and international);
• Tertiary students conducting research.
• Potential employees
• Potential Business Partners
Best Practice Bench Marketing
The following websites are being looked at:
• Korvel Quays - http://www.korvelquays.example/ (preferred look)
• Tidewell Shipping Association - http://www.twa-ships.example/ (like image transition on main page)
• Brolund - http://www.brolund.example (professional look)
• KHW - http://www.kelharbours.example (preferred color: blue in logo)
• Vendlo - http://www.vendlo.example/electronics/tv-video-audio/ (preferred look for links page: image + short text below + visit site link)
Expected Result
• 3 - 5 pages which must include: [1] main page [2] standard page [3] links page
Target Market(s)
The General Public; Members of the organization; Shipping Industry Stakeholders (local, regional and international); Tertiary students conductin
Industry/Entity Type
Shipping

```html
<!DOCTYPE html>
<html lang="en">
<head>
<meta charset="utf-8">
<title>Shipping Industry</title>
<link rel="stylesheet" href="https://fonts.googleapis.com/css2?family=Ubuntu:wght@400;500;700&family=Arimo:wght@400;700&display=swap">
<style>
:root{
  --blue:#0b46c2;
  --blue-dark:#0a2f9a;
  --blue-light:#2f7bf0;
  --orange:#f7a51c;
  --orange-light:#ffc23a;
  --ink:#222;
  --text:#444;
  --footer:#1c1c1c;
  --card:#f3f3f3;
  --line:#dcdcdc;
}
*{box-sizing:border-box;margin:0;padding:0}
html,body{width:970px;height:1200px;overflow:hidden;background:#fff}
body{position:relative;font-family:"Arimo",Arial,sans-serif;color:var(--text)}
.abs{position:absolute}
a{color:inherit;text-decoration:none}

/* top navigation */
.topnav{left:0;top:0;width:970px;height:32px;background:linear-gradient(#2a6fe0,#0a3fb8);border-bottom:3px solid var(--orange)}
.topnav ul{list-style:none;position:absolute;left:94px;top:0;display:flex;height:29px}
.topnav li{font:500 11px "Ubuntu",sans-serif;color:#fff;line-height:29px;padding:0 25px}
.topnav li.active{background:var(--orange);width:81px;text-align:center;padding:0}
.topnav li.n-news{padding-left:28px}

.site-title{left:94px;top:50px;font:700 32px "Ubuntu",sans-serif;color:var(--blue);letter-spacing:.3px}
.follow{left:673px;top:66px;font:700 11px "Ubuntu",sans-serif;color:#222;display:flex;align-items:center;gap:8px}
.follow .dot{width:19px;height:19px;border-radius:4px;display:inline-block}

/* hero */
.hero{left:75px;top:105px;width:813px;height:329px;background:linear-gradient(#a8c8e8 0%,#cfe1f2 45%,#6d7f92 60%,#2f3b46 72%,#7a8a96 100%)}
.hero-panel{left:504px;top:222px;width:394px;height:172px}
.hero-panel h2{position:absolute;left:13px;top:20px;font:700 15px "Ubuntu",sans-serif;color:#fff;white-space:nowrap}
.hero-panel p{position:absolute;left:16px;top:56px;width:366px;font:10px/17px "Arimo",sans-serif;color:#fff}
.btn-orange{background:linear-gradient(var(--orange-light),var(--orange));color:#fff;border:2px solid #fff;border-radius:8px;font:500 12px "Ubuntu",sans-serif;text-align:center}
.hero-panel .btn-orange{position:absolute;left:270px;top:127px;width:98px;height:26px;line-height:22px}

/* intro */
.intro-title{left:76px;top:455px;font:700 17px "Ubuntu",sans-serif;color:var(--ink)}
.intro-title .b{color:var(--blue)}
.intro-title .o{color:var(--orange)}
.intro-photo{left:76px;top:493px;width:151px;height:129px;background:linear-gradient(#b9cde2,#6b7d8e 55%,#1f3d77 80%,#55606a)}
.intro-text{left:239px;top:492px;width:389px;font:10px/20px "Arimo",sans-serif;color:#333;text-align:justify;letter-spacing:.2px}
.intro-text b{color:#111}
.intro-list{left:243px;top:579px;width:390px;display:grid;grid-template-columns:178px 178px;row-gap:4px;list-style:none;font:10px/16px "Arimo",sans-serif;color:#333}
.intro-list li{display:flex;align-items:center;gap:6px}

/* member area */
.member{left:636px;top:452px;width:255px;height:172px;background:linear-gradient(#fff,#f0f0f0);border-top:4px solid var(--blue);border-radius:10px;box-shadow:0 0 3px rgba(0,0,0,.12)}
.member h3{position:absolute;left:21px;top:14px;font:700 17px "Ubuntu",sans-serif;color:var(--blue);letter-spacing:.5px}
.member .rule{position:absolute;left:17px;right:17px;top:44px;border-top:1px dotted #bbb}
.member label{position:absolute;left:19px;font:11px "Arimo",sans-serif;color:#333}
.member .field{position:absolute;left:68px;width:173px;height:23px;border:1px solid #d6d6d6;border-radius:12px;background:#fff}
.member .submit{position:absolute;left:170px;top:126px;width:72px;height:25px;border:0;border-radius:7px;font:700 11px "Ubuntu",sans-serif;line-height:25px;letter-spacing:.5px}

/* news */
.news-head{left:78px;top:641px;display:flex;align-items:center;gap:12px;font:700 17px "Ubuntu",sans-serif;color:#333}
.news-icon{width:24px;height:24px;border-radius:4px;background:var(--orange)}
.card{width:400px;height:133px;background:linear-gradient(#fff,#ececec);border:1px solid #e2e2e2}
.card h4{position:absolute;left:7px;top:11px;font:700 15px "Ubuntu",sans-serif;color:var(--blue);white-space:nowrap}
.card p{position:absolute;left:11px;top:44px;width:278px;font:10px/17px "Arimo",sans-serif;color:#444;text-align:justify;letter-spacing:.2px}
.card .more{position:absolute;left:11px;top:103px;width:94px;height:20px;border-radius:6px;background:linear-gradient(#2f6fe0,#0b3db4);color:#fff;font:500 11px/20px "Ubuntu",sans-serif;padding-left:13px}
.card .more svg{position:absolute;right:9px;top:5px}
.card .thumb{position:absolute;left:298px;top:38px;width:92px;height:92px;border-radius:50%;border:3px solid #fff;box-shadow:0 0 3px rgba(0,0,0,.25);background:linear-gradient(#9cc3e8,#e7eef5 55%,#1b3c5c 70%,#0d2740)}

/* footer */
.footer{left:0;top:984px;width:970px;height:173px;background:var(--footer);border-top:5px solid var(--blue)}
.fcol{top:1006px}
.fcol h5{font:700 15px "Ubuntu",sans-serif;color:var(--orange);margin-bottom:16px}
.fcol ul{list-style:none}
.fcol li{font:700 9.5px/19.4px "Ubuntu",sans-serif;color:#fff;display:flex;align-items:center;gap:6px}
.bottombar{left:0;top:1157px;width:970px;height:43px;background:linear-gradient(#2a6fe0,#0a3fb8);text-align:center;color:#fff}
.bottombar .links{margin-top:6px;font:11px "Ubuntu",sans-serif;word-spacing:2px}
.bottombar .links span{margin:0 22px}
.bottombar .copy{margin-top:5px;font:11px "Ubuntu",sans-serif}
</style>
</head>
<body>

<nav class="abs topnav">
  <ul>
    <li class="active">HOME</li>
    <li class="n-news">NEWS</li>
    <li>CAREER</li>
    <li>SUBSTAINABILTY</li>
    <li>ISSUES</li>
    <li>LINKS</li>
    <li>CONTACT US</li>
  </ul>
</nav>

<div class="abs site-title">Shipping Industry</div>
<div class="abs follow">Follow Us On :-
  <span class="dot" style="background:#f39019"></span>
  <span class="dot" style="background:#4fb6e6"></span>
  <span class="dot" style="background:#3b5ca8"></span>
  <span class="dot" style="background:#17a3e2;border-radius:50%"></span>
</div>

<div class="abs hero" role="img" aria-label="Photo of a loaded container ship docked at a port under cargo cranes"></div>
<div class="abs hero-panel">
  <svg width="394" height="172" style="position:absolute;left:0;top:0">
    <defs><linearGradient id="pg" x1="0" y1="0" x2="0" y2="1"><stop offset="0" stop-color="#3a85f2"/><stop offset="1" stop-color="#0a33a8"/></linearGradient></defs>
    <polygon points="394,-22 394,10 386,10" fill="#3a85f2"/>
    <path d="M0 20 L380 10 L394 10 L384 172 L0 172 Z" fill="url(#pg)"/>
  </svg>
  <h2>Shipping Industry Expands Commerical Network</h2>
  <p>Lorem Ipsum is simply dummy text of the printing and typesetting industry. Lorem Ipsum has been the industry's standard dummy text ever since the 1500s, when an unknown printer took a galley of type and scrambled it to make a type specimen book.</p>
  <a class="btn-orange">Learn more</a>
</div>

<h2 class="abs intro-title">The <span class="b">International Shipping</span> and <span class="o">Information Devlopment</span></h2>
<div class="abs intro-photo" role="img" aria-label="Photo of a cargo ship alongside port cranes"></div>
<p class="abs intro-text"><b>Lorem Ipsum is simply dummy text of the printing and typesetting industry. Lorem Ipsum has been the industry's standard</b> dummy text ever since the 1500s, when an unknown printer took a galley of type and scrambled it to make a type of dummy text</p>
<ul class="abs intro-list">
  <li><svg width="10" height="8"><path d="M0 0L5 4L0 8ZM5 0L10 4L5 8Z" fill="#0b46c2"/></svg>Lorum ipsum is simply dummy</li>
  <li><svg width="10" height="8"><path d="M0 0L5 4L0 8ZM5 0L10 4L5 8Z" fill="#0b46c2"/></svg>Lorum ipsum is simply dummy</li>
  <li><svg width="10" height="8"><path d="M0 0L5 4L0 8ZM5 0L10 4L5 8Z" fill="#0b46c2"/></svg>Lorum ipsum is simply dummy</li>
  <li><svg width="10" height="8"><path d="M0 0L5 4L0 8ZM5 0L10 4L5 8Z" fill="#0b46c2"/></svg>Lorum ipsum is simply dummy</li>
</ul>

<form class="abs member">
  <h3>Member Area</h3>
  <div class="rule"></div>
  <label style="top:65px">Name :</label><span class="field" style="top:59px"></span>
  <label style="top:97px">Email :</label><span class="field" style="top:91px"></span>
  <span class="submit btn-orange">SUBMIT</span>
</form>

<div class="abs news-head">
  <span class="news-icon"></span>
  Latest News
</div>

<article class="abs card" style="left:77px;top:685px">
  <h4>Caribbean Lacks Resources To Combat Oil Spills</h4>
  <p>Lorem Ipsum is simply dummy text of the printing and typesetting industry. Lorem Ipsum has been the industry's standard dummy text ever since the 1500s.</p>
  <a class="more">View more<svg width="8" height="10"><path d="M1 1L6 5L1 9" stroke="#fff" stroke-width="2.2" fill="none"/></svg></a>
  <div class="thumb" role="img" aria-label="Round photo of a container ship at sea"></div>
</article>
<article class="abs card" style="left:492px;top:685px">
  <h4>Caribbean Lacks Resources To Combat Oil Spills</h4>
  <p>Lorem Ipsum is simply dummy text of the printing and typesetting industry. Lorem Ipsum has been the industry's standard dummy text ever since the 1500s.</p>
  <a class="more">View more<svg width="8" height="10"><path d="M1 1L6 5L1 9" stroke="#fff" stroke-width="2.2" fill="none"/></svg></a>
  <div class="thumb" role="img" aria-label="Round photo of a container ship at sea"></div>
</article>
<article class="abs card" style="left:77px;top:838px">
  <h4>Caribbean Lacks Resources To Combat Oil Spills</h4>
  <p>Lorem Ipsum is simply dummy text of the printing and typesetting industry. Lorem Ipsum has been the industry's standard dummy text ever since the 1500s.</p>
  <a class="more">View more<svg width="8" height="10"><path d="M1 1L6 5L1 9" stroke="#fff" stroke-width="2.2" fill="none"/></svg></a>
  <div class="thumb" role="img" aria-label="Round photo of a container ship at sea"></div>
</article>
<article class="abs card" style="left:492px;top:838px">
  <h4>Caribbean Lacks Resources To Combat Oil Spills</h4>
  <p>Lorem Ipsum is simply dummy text of the printing and typesetting industry. Lorem Ipsum has been the industry's standard dummy text ever since the 1500s.</p>
  <a class="more">View more<svg width="8" height="10"><path d="M1 1L6 5L1 9" stroke="#fff" stroke-width="2.2" fill="none"/></svg></a>
  <div class="thumb" role="img" aria-label="Round photo of a container ship at sea"></div>
</article>

<footer class="abs footer"></footer>
<div class="abs fcol" style="left:107px">
  <h5>How we Work</h5>
  <ul><li><svg width="4" height="7"><path d="M0 0L4 3.5L0 7Z" fill="#2f7bf0"/></svg>Service Guarantee</li><li><svg width="4" height="7"><path d="M0 0L4 3.5L0 7Z" fill="#2f7bf0"/></svg>Group Buying</li><li><svg width="4" height="7"><path d="M0 0L4 3.5L0 7Z" fill="#2f7bf0"/></svg>Procurement Process</li><li><svg width="4" height="7"><path d="M0 0L4 3.5L0 7Z" fill="#2f7bf0"/></svg>Benchmarking</li><li><svg width="4" height="7"><path d="M0 0L4 3.5L0 7Z" fill="#2f7bf0"/></svg>Project Management</li></ul>
</div>
<div class="abs fcol" style="left:325px">
  <h5>Our Services</h5>
  <ul><li><svg width="4" height="7"><path d="M0 0L4 3.5L0 7Z" fill="#2f7bf0"/></svg>Service Guarantee</li><li><svg width="4" height="7"><path d="M0 0L4 3.5L0 7Z" fill="#2f7bf0"/></svg>Group Buying</li><li><svg width="4" height="7"><path d="M0 0L4 3.5L0 7Z" fill="#2f7bf0"/></svg>Procurement Process</li><li><svg width="4" height="7"><path d="M0 0L4 3.5L0 7Z" fill="#2f7bf0"/></svg>Benchmarking</li><li><svg width="4" height="7"><path d="M0 0L4 3.5L0 7Z" fill="#2f7bf0"/></svg>Project Management</li></ul>
</div>
<div class="abs fcol" style="left:546px">
  <h5>Why us !</h5>
  <ul><li><svg width="4" height="7"><path d="M0 0L4 3.5L0 7Z" fill="#2f7bf0"/></svg>Service Guarantee</li><li><svg width="4" height="7"><path d="M0 0L4 3.5L0 7Z" fill="#2f7bf0"/></svg>Group Buying</li><li><svg width="4" height="7"><path d="M0 0L4 3.5L0 7Z" fill="#2f7bf0"/></svg>Procurement Process</li><li><svg width="4" height="7"><path d="M0 0L4 3.5L0 7Z" fill="#2f7bf0"/></svg>Benchmarking</li><li><svg width="4" height="7"><path d="M0 0L4 3.5L0 7Z" fill="#2f7bf0"/></svg>Project Management</li></ul>
</div>
<div class="abs fcol" style="left:744px">
  <h5>Why us !</h5>
  <ul><li><svg width="4" height="7"><path d="M0 0L4 3.5L0 7Z" fill="#2f7bf0"/></svg>Service Guarantee</li><li><svg width="4" height="7"><path d="M0 0L4 3.5L0 7Z" fill="#2f7bf0"/></svg>Group Buying</li><li><svg width="4" height="7"><path d="M0 0L4 3.5L0 7Z" fill="#2f7bf0"/></svg>Procurement Process</li><li><svg width="4" height="7"><path d="M0 0L4 3.5L0 7Z" fill="#2f7bf0"/></svg>Benchmarking</li><li><svg width="4" height="7"><path d="M0 0L4 3.5L0 7Z" fill="#2f7bf0"/></svg>Project Management</li></ul>
</div>

<div class="abs bottombar">
  <div class="links">Home<span>|</span>News<span>|</span>Career<span>|</span>Substainabilty<span>|</span>Issues<span>|</span>Links<span>|</span>Contact Us</div>
  <div class="copy">Copyright @ 2012&nbsp; shippingindustry.example. All Right Reserved</div>
</div>

</body>
</html>
```